Website Redesign for a faith-based, not-for-profit health and human services organization

New website design for the Harbor Faith Outreach Hall.
- Current site: www.hfohlp.org -
We are looking for a nice clean, simple, friendly-yet-elegant website layout.
Colors are #f5eed5 (cream), #FFFFFF (white), and all logo colors.
Design a layout for home page
Design a layout for general layouts
-layout only no html needed (preferably a high res PSD file format) -
Main menu should be along top with side navigation for submenu, no side menu on home page.
Also would be open to seeing some updated colors on the logo design, currently the colors are slightly outdated. The Vine of Morning quilt design fits the organization’s mission and the rural farming / Amish-Mennonite-Brethren community around us.

ADDITIONAL PAGES AND MENU STRUCTURE ON NEW SITE

- How to Help
... Volunteer
... Donate Time
... Donate Money
... Donate Supplies
... Current Needs

- Programs

- News & Events
... Upcoming Events
... Upcoming Fundraisers
... Newsletter

- Our Partners

- About Us
... Overview
... Mission
... Staff Directory
... Board of Directors
... Annual Reports

- Contact

Our annual special event is Gather at the Hearth and should be integrated into the home page - see attached logos and banner

Websites with elements we like (from organizations doing similar work), each for a different reason....

1. http://www.kinroutesnet.org
Good design, color, clarity on this site. Multi-dimensional, photos...easy interaction, etc.

2. http://endemptyplates.org
Quite simple, nothing fancy, but some good basic stuff here, and pretty easy to navigate...

3. http://www.folkhubvx.org
Intrigued by the bulletin board design and the way they have their programs broken down to show impact, needs, etc. It has a lot of good information, but is really too verbose, some of the print is too small, etc. Not perfect, but some interesting design elements.

4. http://sharedlarder.org
Site is boring and not very well designed, but it has some of the features that we would like to see at the top, donations, partners, etc.

5. http://www.zenithmealshelf.org
Too many listings on the sidebar - needs to be cleaner & simpler, but a lot of good information and we like the way they show volunteer photos on the Our Helpers Shine page...

About
Harbor Faith Outreach Hall ("HFOH" or “the Center”) is a faith-based non-for-profit health and human services organization that exists as an outreach of and for the Lo-Bray Community School District.
Tagline: Kindness at Work (we work to serve the needs of the ‘least of these’ with compassion).

Mission
Our mission is to see lives transformed and the community enhanced by encouraging the oppressed, defending the cause of the weak and maintaining the rights of the poor - bringing together the resources of a caring community as a demonstration of the good news of Christ.

Company Overview
Harbor Faith Outreach Hall works closely with the community in which it serves. A tremendous value is placed upon the partnerships that have formed with caring people within the community and with organizations that share the goal of bringing together resources to help those who need it most. Individuals, volunteers, churches, corporations, foundations, and government sources all pull together to help make our mission possible.

Since 1996 the Harbor Faith Outreach Hall has collaboratively worked to see our community enhanced, adapting programs and services to meet the changing needs of the community.

Target Market(s)

people needing assistance in local community

Industry/Entity Type

Government

Requirements
Must have
• Good social button integration
Should not have
• No Find Us page like old website it is not needed

```html
<!DOCTYPE html>
<html lang="en">
<head>
<meta charset="utf-8">
<title>Harbor Faith Outreach Hall</title>
<link rel="stylesheet" href="https://fonts.googleapis.com/css2?family=Cinzel:wght@400;700&family=Gelasio&family=Arimo:wght@400;700&family=Gochi+Hand&display=swap">
<style>
:root{
  --cream:#f5eed5;
  --cream-dark:#ece4c9;
  --panel:#eae1c6;
  --brown:#7a4a1c;
  --brown-dark:#4a3526;
  --gold:#d8a53c;
  --text:#3d3a33;
  --muted:#8b8475;
  --link:#7a1f1f;
  --band:#3a3631;
  --footer:#3b3833;
  --donate:#b8431f;
  --white:#ffffff;
}
*{margin:0;padding:0;box-sizing:border-box}
html,body{width:931px;height:1200px;overflow:hidden;background:var(--cream)}
body{position:relative;font-family:"Arimo",Arial,sans-serif;color:var(--text)}
.abs{position:absolute}
a{color:inherit}

.brand{left:165px;top:28px;display:flex;align-items:center;gap:20px}
.brand-mark{width:66px;height:66px;background:var(--gold);border-radius:4px}
.brand-name{font-family:"Cinzel",serif;font-weight:400;color:var(--brown);font-size:19px;line-height:26px;letter-spacing:.5px}

.search{left:571px;top:49px;width:200px;height:24px;border-radius:12px;background:#e4dcc2;box-shadow:inset 0 1px 2px rgba(0,0,0,.15);font-size:8.5px;color:#777;padding:7px 0 0 18px}
.search-btn{position:absolute;right:2px;top:2px;width:20px;height:20px;border-radius:50%;background:#f4efe0;border:1px solid #cfc6ab}

.nav{left:0;top:118px;width:931px;height:42px;background:linear-gradient(#e7e0cb,#ddd5bd);border-bottom:2px solid #cbc2a6}
.nav ul{list-style:none;position:absolute;left:163px;top:0;display:flex;height:42px}
.nav li{font-family:"Gelasio",serif;font-size:12.5px;color:#847b6a;width:107px;text-align:center;line-height:42px;border-right:1px solid #d0c7ad}
.nav li:last-child{border-right:0}
.nav li.current{background:var(--brown-dark);color:var(--white);width:101px}

.hero-band{left:0;top:160px;width:931px;height:256px;background:var(--band)}
.hero{left:148px;top:160px;width:649px;height:256px;background:linear-gradient(135deg,#8f9aa3,#5d6a78 45%,#2f3e6a 70%,#b9b8b3)}
.hero-caption{left:148px;top:356px;width:466px;height:60px;background:rgba(40,38,36,.55);font-family:"Gochi Hand",cursive;color:var(--white);font-size:17px;line-height:20px;text-align:right;padding:10px 22px 0 0}
.hero-caption em{font-style:normal;color:var(--gold)}
.donate{left:614px;top:356px;width:183px;height:60px;background:linear-gradient(#c64d22,#9c3414);color:var(--white);padding:14px 0 0 14px}
.donate b{font-family:"Arimo",sans-serif;font-size:16px;display:flex;align-items:center;gap:8px}
.donate small{display:block;font-size:7.5px;color:#e8b39b;margin:3px 0 0 26px;letter-spacing:.3px}
.hero-arrow{top:283px}

.rule{left:148px;width:649px;height:4px;border-top:1px solid #ddd2b2;border-bottom:1px solid #ddd2b2}

.card{top:451px;width:149px;height:248px;background:var(--white);box-shadow:0 1px 2px rgba(0,0,0,.08)}
.card-photo{height:140px;background:linear-gradient(135deg,#b5b5b5,#6e6e6e)}
.card h2{font-family:"Cinzel",serif;font-weight:400;color:var(--brown);font-size:14px;text-align:center;margin-top:12px}
.card p{font-size:8.3px;line-height:13px;padding:6px 10px 0 12px;color:#333}
.card a{position:absolute;right:8px;bottom:6px;font-size:8px;color:var(--link)}

.overview{left:170px;top:745px;width:360px}
.overview h1{font-family:"Gochi Hand",cursive;font-weight:400;color:var(--brown);font-size:31px}
.overview p{font-size:9.5px;line-height:16.4px;margin-top:14px;color:#3a372f}
.overview a{position:absolute;right:6px;top:168px;font-size:8.5px;color:var(--link)}

.events{left:546px;top:724px;width:240px;height:208px;background:var(--panel);border:1px solid #dcd2b4}
.events h3{font-family:"Cinzel",serif;font-weight:400;font-size:13.5px;color:var(--brown);position:absolute;left:45px;top:30px}
.events-cal{position:absolute;left:14px;top:28px}
.event{position:absolute;left:38px;width:190px;height:40px;border-bottom:1px solid #f4eedc}
.event-date{position:absolute;left:0;top:0;width:26px;text-align:center;font-weight:700;color:var(--muted);font-size:15px;line-height:15px}
.event-date small{display:block;font-size:7.5px;font-weight:400}
.event-title{position:absolute;left:46px;top:2px;font-size:9.5px;color:#444}
.event-note{position:absolute;left:46px;top:16px;font-size:8px;color:#b77d1a}
.events .more{position:absolute;right:16px;bottom:10px;font-size:8.5px;color:var(--link)}

.section-label{left:148px;top:955px;width:649px;text-align:center;font-family:"Cinzel",serif;font-size:9.5px;color:var(--brown)}
.section-label span{background:var(--cream);padding:0 10px;position:relative}
.section-line{left:148px;top:961px;width:649px;height:4px;border-top:1px solid #ddd2b2;border-bottom:1px solid #ddd2b2}

.volunteers{left:157px;top:983px;display:flex;gap:12px}
.volunteer{width:59px;height:58px;background:var(--white);padding:3px;box-shadow:0 1px 2px rgba(0,0,0,.15)}
.volunteer div{width:100%;height:100%;background:linear-gradient(#b07a55,#e2c6a8 55%,#f3f3f3)}
.carousel-shadow{left:170px;top:1055px;width:605px;height:12px;background:radial-gradient(ellipse at top,rgba(0,0,0,.1),transparent 70%)}

.footer{left:0;top:1098px;width:931px;height:102px;background:var(--footer);border-top:6px solid #d8d0b8}
.social{position:absolute;right:160px;top:26px;display:flex;align-items:center;gap:8px;font-size:8px;color:#aaa39a}
.social span{display:flex;align-items:center;gap:3px;color:#c9c2b5}
.social i{width:8px;height:8px;background:#4f6fa4;display:inline-block}
.footer-links{position:absolute;left:498px;top:58px;display:flex;gap:24px;font-size:8.5px;color:var(--gold)}
.footer-links .copy{color:#eee;margin-left:10px}
</style>
</head>
<body>

<header>
  <div class="abs brand">
    <div class="brand-mark"></div>
    <div class="brand-name">Harbor Faith<br>Outreach Hall</div>
  </div>
  <div class="abs search">Enter your search here...
    <span class="search-btn">
      <svg width="20" height="20" viewBox="0 0 20 20"><circle cx="9.5" cy="9.5" r="3" fill="none" stroke="#333" stroke-width="1.3"/><line x1="11.7" y1="11.7" x2="14" y2="14" stroke="#333" stroke-width="1.3"/></svg>
    </span>
  </div>
</header>

<nav class="abs nav">
  <ul>
    <li class="current">Home</li>
    <li>How to Help</li>
    <li>Programs</li>
    <li>Our Partners</li>
    <li>About Us</li>
    <li>Contact</li>
  </ul>
</nav>

<section>
  <div class="abs hero-band"></div>
  <div class="abs hero" role="img" aria-label="Photo of a smiling volunteer unloading a donation box from a trailer"></div>
  <div class="abs hero-caption">We work to serve the needs of<br>the ‘least of these’ <em>with compassion</em></div>
  <div class="abs donate">
    <b><svg width="16" height="14" viewBox="0 0 16 14"><path d="M8 13 1.5 6.5A3.6 3.6 0 0 1 8 2a3.6 3.6 0 0 1 6.5 4.5Z" fill="#7a2a12"/></svg>DONATE TODAY</b>
    <small>JOIN OUR CAMPAIGN</small>
  </div>
  <svg class="abs hero-arrow" style="left:124px" width="12" height="16" viewBox="0 0 12 16"><path d="M9 2 3 8l6 6" fill="none" stroke="#fff" stroke-width="2.5"/></svg>
  <svg class="abs hero-arrow" style="left:809px" width="12" height="16" viewBox="0 0 12 16"><path d="M3 2l6 6-6 6" fill="none" stroke="#fff" stroke-width="2.5"/></svg>
</section>

<div class="abs rule" style="top:430px"></div>

<section>
  <article class="abs card" style="left:157px">
    <div class="card-photo" role="img" aria-label="Black and white photo of volunteers gardening"></div>
    <h2>PROGRAMS</h2>
    <p>Lorem ipsum dolor sit amet, consectetuer adipiscing elit, sed diam nonumm nibh euismod tincidunt.</p>
    <a href="#">Read More</a>
  </article>
  <article class="abs card" style="left:317px">
    <div class="card-photo" role="img" aria-label="Black and white photo of a group presenting a donation check"></div>
    <h2>IMPACT</h2>
    <p>Lorem ipsum dolor sit amet, consectetuer adipiscing elit, sed diam nonumm nibh euismod tincidunt.</p>
    <a href="#">Read More</a>
  </article>
  <article class="abs card" style="left:477px">
    <div class="card-photo" role="img" aria-label="Black and white photo of a volunteer packing boxes"></div>
    <h2>VOLUNTEERS</h2>
    <p>Lorem ipsum dolor sit amet, consectetuer adipiscing elit, sed diam nonumm nibh euismod tincidunt.</p>
    <a href="#">Read More</a>
  </article>
  <article class="abs card" style="left:636px">
    <div class="card-photo" role="img" aria-label="Black and white photo of food pantry shelves"></div>
    <h2>NEEDS</h2>
    <p>Lorem ipsum dolor sit amet, consectetuer adipiscing elit, sed diam nonumm nibh euismod tincidunt.</p>
    <a href="#">Read More</a>
  </article>
</section>

<section class="abs overview">
  <h1>Company Overview</h1>
  <p>Harbor Faith Outreach Hall works closely with the community in which it serves. A tremendous value is placed upon the partnerships that have formed with caring people within the community and with organizations that share the goal of bringing together resources to help those who need it most. Individuals, volunteers, churches, corporations, foundations, and government sources all pull together to help make our mission possible.</p>
  <a href="#">Read More</a>
</section>

<aside class="abs events">
  <svg class="events-cal" width="20" height="20" viewBox="0 0 20 20"><rect x="1.5" y="3" width="17" height="15" rx="1.5" fill="#fff" stroke="#8a7f6a"/><rect x="1.5" y="3" width="17" height="5" fill="#c0443a"/><rect x="5" y="1" width="2" height="4" fill="#8a7f6a"/><rect x="13" y="1" width="2" height="4" fill="#8a7f6a"/></svg>
  <h3>UPCOMING EVENTS</h3>
  <div class="event" style="top:62px"><div class="event-date">09<small>Mar</small></div><div class="event-title">Gather at the Hearth</div><div class="event-note">Lorem ipsum dolor sit amet</div></div>
  <div class="event" style="top:102px"><div class="event-date">09<small>Mar</small></div><div class="event-title">Souper Bowl Fundraiser,</div><div class="event-note">Lorem ipsum dolor sit amet</div></div>
  <div class="event" style="top:142px;border-bottom:0"><div class="event-date">09<small>Mar</small></div><div class="event-title">Souper Bowl Fundraiser,</div><div class="event-note">Lorem ipsum dolor sit amet</div></div>
  <a class="more" href="#">More Events</a>
</aside>

<section>
  <div class="abs section-line"></div>
  <div class="abs section-label"><span>OUR VOLUNTEERS</span></div>
  <svg class="abs" style="left:128px;top:1001px" width="12" height="16" viewBox="0 0 12 16"><path d="M9 2 3 8l6 6" fill="none" stroke="#c2a877" stroke-width="2.5"/></svg>
  <svg class="abs" style="left:804px;top:1001px" width="12" height="16" viewBox="0 0 12 16"><path d="M3 2l6 6-6 6" fill="none" stroke="#c2a877" stroke-width="2.5"/></svg>
  <div class="abs volunteers">
    <div class="volunteer"><div role="img" aria-label="Volunteer portrait"></div></div>
    <div class="volunteer"><div role="img" aria-label="Volunteer portrait"></div></div>
    <div class="volunteer"><div role="img" aria-label="Volunteer portrait"></div></div>
    <div class="volunteer"><div role="img" aria-label="Volunteer portrait"></div></div>
    <div class="volunteer"><div role="img" aria-label="Volunteer portrait"></div></div>
    <div class="volunteer"><div role="img" aria-label="Volunteer portrait"></div></div>
    <div class="volunteer"><div role="img" aria-label="Volunteer portrait"></div></div>
    <div class="volunteer"><div role="img" aria-label="Volunteer portrait"></div></div>
    <div class="volunteer"><div role="img" aria-label="Volunteer portrait"></div></div>
  </div>
  <div class="abs carousel-shadow"></div>
</section>

<footer class="abs footer">
  <div class="social">Find us on
    <span><i></i>Friendwall</span>
    <span><i></i>Chirper</span>
    <span><i></i>Circlely</span>
    <span><i></i>Workline</span>
  </div>
  <div class="footer-links">
    <a href="#">Contact us</a>
    <a href="#">Privacy</a>
    <a href="#">Legal Notices</a>
    <span class="copy">© 2013 HFOH</span>
  </div>
</footer>

</body>
</html>
```